I'm looking for an app for customers to order through

I'm looking for an app for my customers to order products through
Ideally each customer would have a customer number with password
Their profile would come up with a preloaded products they currently order
From there they can select the product they require and volume needed for delivery
I would also like an option for them to go to a full product range if they are looking for Ideas or a product they don't currently use
Once the order is completed a copy of the order is them e-mailed to my distribution facilities and a confirmation sent to the customer by e-mail and/or SMS
Current product list is approx 1000 items
Current customers is 80 with expectations to expand to 200
On average current products ordered by each customer is is between 4-8 items
Ordering units are done by both weight and pieces/units

Target Market(s)

Food service outlets,
Restaurant , Hotels, catering companies, clubs, take away shops, cafes
Retail outlets

Number of Pages Required

1 page

Font styles to use
Sans Serif

Colors
abd037

Requirements
Must have
• Customer log in with Password 4 - 6 digit
• Customer order history
Nice to have
• Area for promotions / specials on a weekly / monthly basis

```html
<!DOCTYPE html>
<html lang="en">
<head>
<meta charset="utf-8">
<title>Wholesale Ordering App – Profile and Products</title>
<link href="https://fonts.googleapis.com/css2?family=Roboto:wght@300;400;500&display=swap" rel="stylesheet">
<style>
  :root{
    --canvas:#f4f4f4;
    --surface:#ffffff;
    --brand-green:#388e3c;
    --accent-green:#2e8b32;
    --ink:#222222;
    --muted:#7a7a7a;
    --edit-red:#d32f2f;
    --butter:#1449a6;
    --oil:#ef6c00;
    --spice:#ff8f00;
    --cheese:#8a4a22;
    --goat:#e53935;
    --herb:#0796a6;
    --brand-red:#c41f24;
    --brand-dark:#231f20;
    --brand-pale:#dfe3e6;
  }
  *{box-sizing:border-box;margin:0;padding:0}
  html,body{width:1200px;height:1051px;overflow:hidden}
  body{background:var(--canvas);font-family:"Roboto",Arial,sans-serif;color:var(--ink);position:relative}

  .screen{position:absolute;top:28px;width:560px;height:994px;background:var(--surface);overflow:hidden;box-shadow:0 1px 4px rgba(0,0,0,.15)}
  .screen--profile{left:28px}
  .screen--catalog{left:612px}

  .menu-icon{position:absolute;left:23px;top:22px;width:38px;height:28px}

  /* profile */
  .profile-cover{position:absolute;left:0;top:0;width:560px;height:358px;background:linear-gradient(100deg,#3a3a3a 0%,#1c1c1c 35%,#5a5a5a 60%,#2a2a2a 100%)}
  .edit-button{position:absolute;left:466px;top:323px;width:68px;height:68px;border-radius:50%;background:var(--edit-red);box-shadow:0 3px 8px rgba(0,0,0,.3);display:flex;align-items:center;justify-content:center}
  .profile-name{position:absolute;left:26px;top:372px;font-size:42px;font-weight:400;letter-spacing:.2px}
  .profile-city{position:absolute;left:29px;top:432px;font-size:19px;color:var(--accent-green)}
  .stat{position:absolute;top:492px}
  .stat-value{font-size:29px;font-weight:400}
  .stat-label{font-size:17px;color:var(--muted);margin-top:4px;letter-spacing:.3px}
  .section-title{position:absolute;left:26px;font-size:17px;font-weight:400}
  .section-more{position:absolute;right:27px;font-size:17px;color:var(--accent-green);letter-spacing:.6px}

  .card-row{position:absolute;left:26px;display:flex;gap:10px}
  .card{flex:0 0 182px;display:flex;flex-direction:column;box-shadow:0 1px 3px rgba(0,0,0,.3);border-radius:2px;overflow:hidden}
  .card-image{flex:1}
  .card-label{position:relative;height:78px;padding:14px 12px 0;color:#fff}
  .card-name{font-size:21px;font-weight:400;line-height:1.1}
  .card-price{font-size:16px;font-weight:300;margin-top:5px}
  .card-basket{position:absolute;right:12px;bottom:13px;width:15px;height:13px}
  .card--dim .card-name,.card--dim .card-price{opacity:.55}
  .card--dim .card-name{opacity:.6}

  .recent-profile{top:630px;height:340px}
  .products-row{top:95px;height:340px}
  .recent-catalog{top:740px;height:228px}

  .bg-cheese{background:var(--cheese)}
  .bg-goat{background:var(--goat)}
  .bg-herb{background:var(--herb)}
  .bg-butter{background:var(--butter)}
  .bg-oil{background:var(--oil)}
  .bg-spice{background:var(--spice)}

  .img-cheese{background:linear-gradient(160deg,#2a1c12 0%,#b07a45 40%,#6b4424 70%,#2a1a10 100%)}
  .img-goat{background:linear-gradient(160deg,#555 0%,#b5525a 35%,#8c3b40 60%,#4a4040 100%)}
  .img-herb{background:linear-gradient(160deg,#f5f5f5 0%,#5aa23a 40%,#2e7d22 75%,#1f5d18 100%)}
  .img-butter{background:linear-gradient(160deg,#0e1530 0%,#efe3a6 40%,#e8d88a 65%,#1a1d2a 100%)}
  .img-oil{background:linear-gradient(180deg,#161616 0%,#2a1a1a 40%,#a03018 70%,#e8a020 100%)}
  .img-spice{background:linear-gradient(160deg,#3a2c3a 0%,#d8d0c8 30%,#d98a2a 60%,#b66a18 100%)}

  /* catalog */
  .app-bar{position:absolute;left:0;top:0;width:560px;height:70px;background:var(--brand-green)}
  .app-title{position:absolute;left:81px;top:22px;font-size:20px;color:#fff;letter-spacing:.4px}
  .search-icon{position:absolute;right:20px;top:22px;width:26px;height:26px}

  .brand-row{position:absolute;left:26px;top:510px;height:155px;display:flex;gap:10px}
  .brand-tile{height:155px;display:flex;align-items:center;justify-content:center;box-shadow:0 1px 3px rgba(0,0,0,.3);border-radius:2px;gap:8px}
  .brand-tile--red{width:158px;background:var(--brand-red)}
  .brand-tile--dark{width:259px;background:var(--brand-dark)}
  .brand-tile--pale{width:160px;background:var(--brand-pale);justify-content:flex-start;padding-left:34px}
  .brand-name{font-size:22px;font-weight:500;letter-spacing:.5px}
  .brand-tile--red .brand-name{color:#fff}
  .brand-tile--dark .brand-name{color:#c9a655;font-size:28px}
  .brand-tile--pale .brand-name{color:#1a5fa8;font-size:30px}
  .brand-dot{width:12px;height:12px;border-radius:50%;background:#f3d27a}
</style>
</head>
<body>

<svg width="0" height="0" style="position:absolute">
  <defs>
    <symbol id="basket" viewBox="0 0 15 13">
      <path d="M0 5h15l-2 8H2z M4 5l3.5-5 3.5 5" fill="currentColor" stroke="currentColor" stroke-width="1"/>
    </symbol>
    <symbol id="menu" viewBox="0 0 38 28">
      <g stroke="#fff" stroke-width="2.2">
        <line x1="0" y1="2" x2="38" y2="2"/><line x1="0" y1="9" x2="32" y2="9"/>
        <line x1="0" y1="16" x2="26" y2="16"/><line x1="0" y1="23" x2="18" y2="23"/>
      </g>
    </symbol>
  </defs>
</svg>

<section class="screen screen--profile">
  <div class="profile-cover" role="img" aria-label="Black and white portrait photo of the customer by a window"></div>
  <svg class="menu-icon"><use href="#menu"/></svg>
  <div class="edit-button">
    <svg width="26" height="26" viewBox="0 0 26 26"><path d="M4 22l1.5-6L17 4.5l4.5 4.5L10 20.5z M15 6.5l4.5 4.5" fill="none" stroke="#fff" stroke-width="2" stroke-linejoin="round"/></svg>
  </div>
  <h1 class="profile-name">Daniel Reyes</h1>
  <p class="profile-city">New York</p>
  <div class="stat" style="left:26px"><div class="stat-value">20</div><div class="stat-label">Fulfilled Orders</div></div>
  <div class="stat" style="left:305px"><div class="stat-value">12</div><div class="stat-label">Pending Orders</div></div>
  <h2 class="section-title" style="top:588px">Recent Orders</h2>
  <div class="card-row recent-profile">
    <article class="card card--dim"><div class="card-image img-cheese" role="img" aria-label="Aged cheese wheels on wooden shelves"></div><div class="card-label bg-cheese"><div class="card-name">Cheese</div><div class="card-price">$300</div><svg class="card-basket" style="color:#e8c8a8"><use href="#basket"/></svg></div></article>
    <article class="card"><div class="card-image img-goat" role="img" aria-label="Raw goat meat with rosemary and chilli"></div><div class="card-label bg-goat"><div class="card-name">Goat Meat</div><div class="card-price">$800</div><svg class="card-basket" style="color:#ffd0d0"><use href="#basket"/></svg></div></article>
    <article class="card"><div class="card-image img-herb" role="img" aria-label="Fresh basil leaves"></div><div class="card-label bg-herb"><div class="card-name">Natural Herbs</div><div class="card-price">$100</div></div></article>
  </div>
</section>

<section class="screen screen--catalog">
  <header class="app-bar">
    <svg class="menu-icon"><use href="#menu"/></svg>
    <span class="app-title">All Products</span>
    <svg class="search-icon" viewBox="0 0 26 26"><circle cx="10" cy="10" r="7.5" fill="none" stroke="#fff" stroke-width="2.5"/><line x1="15.5" y1="15.5" x2="24" y2="24" stroke="#fff" stroke-width="2.8"/></svg>
  </header>

  <div class="card-row products-row">
    <article class="card card--dim"><div class="card-image img-butter" role="img" aria-label="Blocks of butter in a bowl"></div><div class="card-label bg-butter"><div class="card-name" style="opacity:.75">Butter</div><div class="card-price" style="opacity:.7">$20 / kg</div><svg class="card-basket" style="color:#8fb4ff"><use href="#basket"/></svg></div></article>
    <article class="card card--dim"><div class="card-image img-oil" role="img" aria-label="Bottles of oil with chilli and citrus"></div><div class="card-label bg-oil"><div class="card-name">Meat Oil</div><div class="card-price">$40 / bottle</div><svg class="card-basket" style="color:#ffc080"><use href="#basket"/></svg></div></article>
    <article class="card card--dim"><div class="card-image img-spice" role="img" aria-label="Bowls of ground spices"></div><div class="card-label bg-spice"><div class="card-name" style="opacity:.75">Spices</div><div class="card-price">$10 / kg</div></div></article>
  </div>

  <h2 class="section-title" style="top:468px">Top Brands</h2>
  <span class="section-more" style="top:469px">MORE</span>
  <div class="brand-row">
    <div class="brand-tile brand-tile--red"><span class="brand-name">Plume Farm</span></div>
    <div class="brand-tile brand-tile--dark"><span class="brand-dot"></span><span class="brand-name">Highmoor</span></div>
    <div class="brand-tile brand-tile--pale"><span class="brand-name">Coastline</span></div>
  </div>

  <h2 class="section-title" style="top:698px">Recent Orders</h2>
  <span class="section-more" style="top:699px">MORE</span>
  <div class="card-row recent-catalog">
    <article class="card card--dim"><div class="card-image img-cheese" role="img" aria-label="Aged cheese wheels on wooden shelves"></div><div class="card-label bg-cheese"><div class="card-name">Cheese</div><div class="card-price">$300</div><svg class="card-basket" style="color:#e8c8a8"><use href="#basket"/></svg></div></article>
    <article class="card"><div class="card-image img-goat" role="img" aria-label="Raw goat meat with rosemary and chilli"></div><div class="card-label bg-goat"><div class="card-name">Goat Meat</div><div class="card-price">$800</div><svg class="card-basket" style="color:#ffd0d0"><use href="#basket"/></svg></div></article>
    <article class="card"><div class="card-image img-herb" role="img" aria-label="Fresh basil leaves"></div><div class="card-label bg-herb"><div class="card-name">Natural Herbs</div><div class="card-price">$100</div></div></article>
  </div>
</section>

</body>
</html>
```